Marrowfield Contracting Business Cards

Front of card:

Full Logo
Name
Address
Office Phone
Cell Phone
Email
Website

Back:
Logo Mark in background
List and markets and services performed

```html
<!DOCTYPE html>
<html lang="en">
<head>
<meta charset="utf-8">
<title>Marrowfield Contracting – Business Cards</title>
<link rel="stylesheet" href="https://fonts.googleapis.com/css2?family=Montserrat:wght@400;500;600;700&display=swap">
<style>
  :root {
    --brand-red: #d92323;
    --ink: #2e2e2e;
    --ink-soft: #3a3a3a;
    --paper: #ffffff;
    --page: #f1f1f1;
  }
  * { box-sizing: border-box; margin: 0; padding: 0; }
  html, body {
    width: 1200px; height: 1200px; overflow: hidden;
    background: var(--page);
    font-family: "Montserrat", Arial, sans-serif;
  }
  .canvas { position: relative; width: 1200px; height: 1200px; }

  .card {
    position: absolute;
    width: 571px; height: 367px;
    border-radius: 9px;
    overflow: hidden;
  }

  /* Front */
  .card--front { left: 83px; top: 263px; background: var(--paper); }
  .front__accent { position: absolute; left: 0; top: 32px; width: 13px; height: 70px; background: var(--brand-red); }
  .front__tick { position: absolute; left: 36px; top: 53px; width: 2px; height: 31px; background: var(--ink); }
  .front__name {
    position: absolute; left: 52px; top: 44px;
    font-size: 31px; font-weight: 500; line-height: 1; color: var(--ink); letter-spacing: 0.3px;
  }
  .front__title { position: absolute; left: 55px; top: 78px; font-size: 11px; color: var(--ink); }

  .brand-name {
    position: absolute; left: 378px; top: 46px;
    display: flex; align-items: center; gap: 6px;
  }
  .brand-name__dot { width: 30px; height: 30px; border-radius: 50%; background: var(--brand-red); flex: none; }
  .brand-name__text {
    font-size: 12px; font-weight: 700; line-height: 1.15; color: var(--brand-red); letter-spacing: 0.3px;
  }

  .front__rule-thin { position: absolute; left: 28px; top: 117px; width: 506px; height: 2px; background: var(--brand-red); }
  .front__rule-bold { position: absolute; left: 28px; top: 115px; width: 233px; height: 6px; background: var(--brand-red); }

  .contact { position: absolute; left: 0; width: 100%; height: 36px; display: flex; align-items: center; }
  .contact__icon { position: absolute; left: 28px; width: 24px; height: 24px; fill: var(--ink); }
  .contact__divider { position: absolute; left: 63px; width: 2px; height: 34px; background: var(--ink); }
  .contact__text { position: absolute; left: 81px; font-size: 12.5px; line-height: 1.4; color: var(--ink-soft); }
  .contact--phone { top: 142px; }
  .contact--mail { top: 197px; }
  .contact--place { top: 256px; }
  .contact--web { top: 302px; }

  /* Back */
  .card--back { left: 573px; top: 561px; background: var(--brand-red); color: var(--paper); text-align: center; }
  .back__mark {
    position: absolute; left: 227px; top: 27px;
    width: 112px; height: 112px; border-radius: 50%;
    border: 11px solid var(--paper);
  }
  .back__name {
    position: absolute; left: 0; top: 182px; width: 100%;
    font-weight: 700; line-height: 1.05; letter-spacing: 1.5px;
  }
  .back__name-main { display: block; font-size: 33px; }
  .back__name-sub { display: block; font-size: 24px; }
  .back__rule-row {
    position: absolute; left: 163px; top: 251px;
    display: flex; align-items: center; gap: 12px;
  }
  .back__rule { width: 189px; height: 2px; background: var(--paper); }
  .back__llc { font-size: 12px; font-weight: 700; letter-spacing: 3px; }

  .services {
    position: absolute; left: 0; top: 284px; width: 100%;
    font-size: 12.5px; font-weight: 600; line-height: 20px; letter-spacing: 0.2px;
  }
  .services__line { display: flex; justify-content: center; }
  .services__item { padding: 0 5px; }
  .services__item + .services__item { border-left: 1.5px solid var(--paper); }

  .back__web {
    position: absolute; left: 168px; top: 337px; width: 255px; height: 17px;
    border-radius: 9px; background: var(--paper); color: var(--brand-red);
    font-size: 11.5px; font-weight: 700; line-height: 17px;
  }
</style>
</head>
<body>
<main class="canvas">

  <section class="card card--front" aria-label="Business card front">
    <div class="front__accent"></div>
    <div class="front__tick"></div>
    <h1 class="front__name">YOUR NAME</h1>
    <p class="front__title">Ceo</p>

    <div class="brand-name">
      <span class="brand-name__dot"></span>
      <span class="brand-name__text">MARROWFIELD<br>CONTRACTING LLC</span>
    </div>

    <div class="front__rule-thin"></div>
    <div class="front__rule-bold"></div>

    <div class="contact contact--phone">
      <svg class="contact__icon" viewBox="0 0 24 24" aria-hidden="true"><path d="M6.6 3.5l2.6 3.3c.4.5.4 1.2 0 1.7L8 10c1 2.3 3.7 5 6 6l1.5-1.2c.5-.4 1.2-.4 1.7 0l3.3 2.6c.5.4.6 1.1.2 1.6l-1.4 1.9c-.5.7-1.4 1-2.2.8C10.6 20.2 3.8 13.4 2.3 6.9c-.2-.8.1-1.7.8-2.2L5 3.3c.5-.4 1.2-.3 1.6.2z"/></svg>
      <span class="contact__divider"></span>
      <span class="contact__text">484-312-7046</span>
    </div>

    <div class="contact contact--mail">
      <svg class="contact__icon" viewBox="0 0 24 24" aria-hidden="true"><path d="M2 5h20v14H2z M3.5 6.5l8.5 6.5 8.5-6.5" fill="none" stroke="currentColor"/><path d="M2 5h20v2l-10 7L2 7z"/><path d="M2 8.5l10 7 10-7V19H2z"/></svg>
      <span class="contact__divider"></span>
      <span class="contact__text">info@marrowfieldcontracting.com</span>
    </div>

    <div class="contact contact--place">
      <svg class="contact__icon" viewBox="0 0 24 24" aria-hidden="true"><path d="M12 2a6.5 6.5 0 0 0-6.5 6.5C5.5 13.4 12 22 12 22s6.5-8.6 6.5-13.5A6.5 6.5 0 0 0 12 2zm0 9a2.5 2.5 0 1 1 0-5 2.5 2.5 0 0 1 0 5z"/></svg>
      <span class="contact__divider"></span>
      <span class="contact__text">1475 Millrace Rd., Ashby,<br>PA 18102</span>
    </div>

    <div class="contact contact--web">
      <svg class="contact__icon" viewBox="0 0 24 24" aria-hidden="true"><path fill-rule="evenodd" d="M12 2a10 10 0 1 0 0 20 10 10 0 0 0 0-20zm-1 2.1C9.7 5.6 8.9 7.6 8.7 11H4.1A8 8 0 0 1 11 4.1zm2 0A8 8 0 0 1 19.9 11h-4.6c-.2-3.4-1-5.4-2.3-6.9zM10.7 11c.2-3 1-4.8 1.3-5.4.3.6 1.1 2.4 1.3 5.4zm-6.6 2h4.6c.2 3.4 1 5.4 2.3 6.9A8 8 0 0 1 4.1 13zm6.6 0h2.6c-.2 3-1 4.8-1.3 5.4-.3-.6-1.1-2.4-1.3-5.4zm4.6 0h4.6a8 8 0 0 1-6.9 6.9c1.3-1.5 2.1-3.5 2.3-6.9z"/></svg>
      <span class="contact__divider"></span>
      <span class="contact__text">www.marrowfieldcontracting.com</span>
    </div>
  </section>

  <section class="card card--back" aria-label="Business card back">
    <div class="back__mark"></div>
    <h2 class="back__name">
      <span class="back__name-main">MARROWFIELD</span>
      <span class="back__name-sub">CONTRACTING</span>
    </h2>
    <div class="back__rule-row">
      <span class="back__rule"></span>
      <span class="back__llc">LLC</span>
    </div>

    <div class="services">
      <div class="services__line">
        <span class="services__item">CONCRATE STRUCTURES</span>
        <span class="services__item">CONCRATE PAVEMENT</span>
        <span class="services__item">BRIDGES</span>
      </div>
      <div class="services__line">
        <span class="services__item">CONCRATE CURB</span>
        <span class="services__item">SITE CONCRETE</span>
        <span class="services__item">UNIQUE AND COMPLICATED PROJECT</span>
      </div>
    </div>

    <div class="back__web">www.marrowfieldcontracting.com</div>
  </section>

</main>
</body>
</html>
```